Etiketten für Weinflasche
Zielgruppe
HANDARBEIT
HAT SEELE.
»80 % gibt uns die Natur vor,
für die restlichen 20 % geben wir alles!«
Volker Brandhuber
Seit über 125 Jahren ist die Rotweinstadt Ingelheim Sitz unseres Familienbetriebes. Im alten Ober-Ingelheimer Schulhaus gelegen, betreiben wir das Weingut in der nunmehr 5. Generation. Unser hoher Qualitätsanspruch und Traditionsbewusstsein wird von Kennern eines guten Weines geschätzt. Zusammen mit der Natur und so schonend wie möglich bewirtschaften wir die rund 15 ha Weinberge in den besten Lagen Ingelheims.
Ganz in der Tradition Karls des Großen, der die Rotweinreben um 800 n. Chr. nach Ingelheim brachte, sind die Spät- und Frühburgunder die Spezialitäten unseres Hauses. Seit 2015 sind wir Träger des „Goldenen Traubenpokals' des Weinkulturmagazins Korkla. Das macht uns stolz und gibt uns Energie. Auch die Rieslinge und die weißen Burgundersorten stehen im Fokus und werden mit viel Gefühl zum Detail gekeltert. Den geselligen Mittelpunkt des Weinguts bildet unser über hundert Jahre alter Pavillon. Er steht symbolisch für uns als gastliche Weinfamilie und vertritt unser Weingut auch nach außen auf unseren Etiketten.
Aufgabenstellung
Ein Wein für FRANKFURTER
Wir möchten für einen führende Marktis-Gruppe in Frankfurt eine Weißwein-Sonderedition entwickeln.
Es soll ein Label sein, womit sich jeder Frankfurter identifizieren kann (Skyline gab es schon mal ist aber nicht ausgeschlossen) und dazu animiert wird die Weinflasche blind zu kaufen.
Die Rebsorte soll auf dem Vorderetikett genannt werden. Es ist ein Grauburgunder oder Grauer Burgunder. Der Wein soll ein schönes Mitbringsel oder auch für den eigenen Genuss sein. Die Flasche wird sich im mittleren Preissegment bewegen +/- 10€ im Verkauf. Zielgruppe 40-65 Jahre alt.
Es gibt drei mögliche Etikettengrößen.
Variante 1: Bestehendes Brandhuber-Etikett mit Streifen (wie in der Anlage)
Variante 2: Vorder- und Rückenetikett mit je 7cm x 7cm oder
Variante 3: Vorderetikett (9cm Breit x 6cm hoch) und Rückenetikett (7cm Breit x 6cm hoch)
Die Rückseite kann ein : gestalterisches Element vom Vorderetikett beinhalten, ist aber durch die gesetzlichen Angaben und den EAN-Code schon ziemlich ausgelastet. Es zum größten Teil um das Vorderetikett.
Die Kapsel am Flaschenhals ist weiß mit gelber Markierung und es gibt eine gelbe Kapsel mit weißer Markierung. Diese ist beiden sind fix, da der Wein schon abgefüllt ist. Es ist eine Burgunderflasche.
Ein Flaschenbild stelle ich zur Verfügung.

```html
<!DOCTYPE html>
<html lang="de">
<head>
<meta charset="utf-8">
<title>Grauburgunder Jahrgang 2021 – Etikett</title>
<link href="https://fonts.googleapis.com/css2?family=Montserrat:wght@300;400;800&family=EB+Garamond:ital,wght@0,400;1,400&display=swap" rel="stylesheet">
<style>
  :root {
    --backdrop: #172639;
    --paper: #fbfbf9;
    --ink: #1b1b1b;
    --amber: #f2a51c;
    --amber-deep: #e08a10;
    --butter: #f7d27a;
    --wine: #9b3b38;
  }
  * { box-sizing: border-box; margin: 0; padding: 0; }
  html, body { width: 1200px; height: 860px; overflow: hidden; }
  body {
    background: var(--backdrop);
    display: flex;
    align-items: center;
    justify-content: center;
    font-family: "Montserrat", sans-serif;
    color: var(--ink);
  }
  .label {
    position: relative;
    width: 560px;
    height: 760px;
    background: var(--paper);
    overflow: hidden;
  }
  .corner-top {
    position: absolute; top: 0; left: 0;
    width: 150px; height: 170px;
  }
  .corner-bottom {
    position: absolute; right: 0; bottom: 0;
    width: 220px; height: 200px;
  }
  .edge-squares {
    position: absolute;
    top: 40px;
    display: flex;
    flex-direction: column;
    gap: 62px;
  }
  .edge-squares span { display: block; width: 40px; height: 58px; }
  .edge-squares--right { right: 0; }
  .edge-squares--right span { background: var(--butter); }
  .edge-squares--left { left: 0; top: 250px; }
  .edge-squares--left span { background: var(--wine); }
  .emblem {
    position: absolute;
    top: 140px; left: 130px;
    width: 300px; height: 300px;
    border-radius: 50%;
    border: 2px solid var(--ink);
    background: radial-gradient(circle at 50% 45%, #ffffff 0%, #eeeeee 100%);
  }
  .wine-info {
    position: absolute;
    left: 110px; top: 478px;
  }
  .wine-info__tag {
    font-weight: 300;
    font-size: 22px;
    letter-spacing: 2px;
    line-height: 1;
  }
  .wine-info__variety {
    font-weight: 800;
    font-size: 42px;
    letter-spacing: 0.5px;
    line-height: 1.05;
  }
  .wine-info__vintage {
    font-weight: 300;
    font-size: 36px;
    line-height: 1.1;
  }
  .wine-info__motto {
    margin-top: 8px;
    font-family: "EB Garamond", serif;
    font-style: italic;
    font-size: 16px;
    line-height: 1.25;
  }
  .maker {
    position: absolute;
    left: 110px; bottom: 46px;
    display: flex;
    align-items: center;
    gap: 14px;
    z-index: 1;
  }
  .maker__mark { width: 30px; height: 30px; background: var(--ink); }
  .maker__name {
    font-family: "EB Garamond", serif;
    font-size: 24px;
    letter-spacing: 2px;
    text-transform: uppercase;
    white-space: nowrap;
  }
</style>
</head>
<body>
  <main class="label">
    <svg class="corner-top" viewBox="0 0 150 170" aria-hidden="true">
      <polygon points="0,0 150,0 0,170" fill="var(--amber)"/>
    </svg>

    <div class="edge-squares edge-squares--right" aria-hidden="true">
      <span></span><span></span><span></span><span></span>
    </div>
    <div class="edge-squares edge-squares--left" aria-hidden="true">
      <span></span><span></span><span></span><span></span>
    </div>

    <div class="emblem" role="img" aria-label="Linienzeichnung: Frankfurter Skyline mit Türmen und Brücke über Weinbergen in einem Blatt"></div>

    <section class="wine-info">
      <p class="wine-info__tag">handarbeit</p>
      <h1 class="wine-info__variety">Grauburgunder</h1>
      <p class="wine-info__vintage">Jahrgang 2021</p>
      <p class="wine-info__motto">80 % gibt uns die Natur vor,<br>für die restlichen 20 % geben wir alles</p>
    </section>

    <svg class="corner-bottom" viewBox="0 0 220 200" aria-hidden="true">
      <path d="M220,0 C130,35 60,110 35,200 L220,200 Z" fill="var(--amber)"/>
      <path d="M220,60 C160,85 115,145 105,200 L220,200 Z" fill="var(--amber-deep)"/>
    </svg>

    <div class="maker">
      <span class="maker__mark" aria-hidden="true"></span>
      <span class="maker__name">Brandhuber</span>
    </div>
  </main>
</body>
</html>
```